Salon and Spa Distributor Business Card

Need a business card. We are are distributor in the salon and spa industry. We identify with natural beauty. Need a card with:
Company Name: Petal Haven"
Title: "President & CEO"
Address
Company Phone number
email
website
Tag Line:" The Professional Salon Source"

Industry/Entity Type

Business

Contact Information for Business Card

Name: Lena Morcott
Title: "President & CEO"
Address: 317 Birchfield Ln, Oakvane, NJ 07481
Company Phone number: 800-463-9152
email: lenamorcott@petalhaven-example.com
website: www.petalhaven-example.com

Requirements
Should not have
• No black backgrounds

```html
<!DOCTYPE html>
<html lang="en">
<head>
<meta charset="utf-8">
<title>Petal Haven — Business Card</title>
<link rel="stylesheet" href="https://fonts.googleapis.com/css2?family=Didact+Gothic&family=Encode+Sans+Condensed:wght@500&family=Tinos&display=swap">
<style>
  :root {
    --page-bg: #e9ebe8;
    --card-white: #ffffff;
    --card-shade: #dcdcdc;
    --brand-green: #3f8f3c;
    --brand-green-bright: #4fa843;
    --soft-green: rgba(120, 185, 110, 0.22);
    --ink: #1b1b1b;
    --ink-soft: #2a2a2a;
  }
  * { box-sizing: border-box; margin: 0; padding: 0; }
  html, body {
    width: 1200px;
    height: 997px;
    overflow: hidden;
    background: var(--page-bg);
  }
  .canvas {
    position: relative;
    width: 1200px;
    height: 997px;
  }
  .card {
    position: absolute;
    top: 350px;
    width: 527px;
    height: 315px;
    border-radius: 18px;
    overflow: hidden;
    background: var(--card-white);
    box-shadow: 0 6px 18px rgba(0, 0, 0, 0.12);
  }
  .card--front {
    left: 66px;
    background: linear-gradient(90deg, var(--card-shade) 0%, var(--card-white) 38%, var(--card-white) 100%);
  }
  .card--back { left: 614px; }

  .card__decor {
    position: absolute;
    width: 340px;
    height: 340px;
    border-radius: 50%;
    background: var(--soft-green);
  }
  .card--front .card__decor { left: 360px; top: 10px; }
  .card--back .card__decor { left: -190px; top: 10px; }

  /* Front */
  .front__mark {
    position: absolute;
    left: 150px;
    top: 40px;
    width: 120px;
    height: 120px;
    border-radius: 50%;
    background: var(--brand-green-bright);
  }
  .front__name {
    position: absolute;
    left: 64px;
    top: 212px;
    width: 290px;
    text-align: center;
    font-family: "Didact Gothic", sans-serif;
    font-size: 41px;
    color: var(--brand-green);
    line-height: 1;
    white-space: nowrap;
  }
  .front__tagline {
    position: absolute;
    left: 38px;
    top: 265px;
    font-family: "Encode Sans Condensed", sans-serif;
    font-weight: 500;
    font-size: 21px;
    letter-spacing: 1.6px;
    color: var(--ink);
    white-space: nowrap;
  }

  /* Back */
  .back__brand {
    position: absolute;
    right: 28px;
    top: 46px;
    display: flex;
    align-items: center;
    gap: 12px;
  }
  .back__mark {
    width: 58px;
    height: 58px;
    border-radius: 50%;
    background: var(--brand-green-bright);
  }
  .back__brand-name {
    font-family: "Didact Gothic", sans-serif;
    font-size: 24px;
    color: var(--brand-green);
  }
  .back__person {
    position: absolute;
    right: 35px;
    top: 130px;
    text-align: right;
  }
  .back__person-name {
    font-family: "Didact Gothic", sans-serif;
    font-size: 24px;
    color: var(--brand-green);
    line-height: 1.05;
  }
  .back__person-title {
    font-family: "Tinos", serif;
    font-size: 16px;
    color: var(--ink-soft);
  }
  .back__contacts {
    position: absolute;
    right: 32px;
    top: 205px;
    list-style: none;
  }
  .contact {
    display: flex;
    align-items: center;
    justify-content: flex-end;
    gap: 12px;
    height: 22px;
    margin-bottom: 11px;
    font-family: "Didact Gothic", sans-serif;
    font-size: 15px;
    color: var(--ink);
    white-space: nowrap;
  }
  .contact__icon {
    width: 23px;
    height: 23px;
    border-radius: 50%;
    background: var(--brand-green);
    display: flex;
    align-items: center;
    justify-content: center;
    flex-shrink: 0;
  }
  .contact__icon svg { width: 13px; height: 13px; fill: #fff; }
</style>
</head>
<body>
<main class="canvas">
  <section class="card card--front" aria-label="Card front">
    <div class="card__decor" aria-hidden="true"></div>
    <div class="front__mark" aria-hidden="true"></div>
    <p class="front__name">Petal Haven</p>
    <p class="front__tagline">The Professional Salon Source</p>
  </section>

  <section class="card card--back" aria-label="Card back">
    <div class="card__decor" aria-hidden="true"></div>
    <div class="back__brand">
      <div class="back__mark" aria-hidden="true"></div>
      <span class="back__brand-name">Petal Haven</span>
    </div>
    <div class="back__person">
      <p class="back__person-name">Lena Morcott</p>
      <p class="back__person-title">President &amp; CEO</p>
    </div>
    <ul class="back__contacts">
      <li class="contact">
        <span>800-463-9152</span>
        <span class="contact__icon"><svg viewBox="0 0 24 24" aria-hidden="true"><path d="M6.6 10.8a15.1 15.1 0 0 0 6.6 6.6l2.2-2.2c.3-.3.7-.4 1-.2 1.1.4 2.3.6 3.6.6.6 0 1 .4 1 1V20c0 .6-.4 1-1 1A17 17 0 0 1 3 4c0-.6.4-1 1-1h3.5c.6 0 1 .4 1 1 0 1.3.2 2.5.6 3.6.1.3 0 .7-.2 1z"/></svg></span>
      </li>
      <li class="contact">
        <span>lenamorcott@petalhaven-example.com</span>
        <span class="contact__icon"><svg viewBox="0 0 24 24" aria-hidden="true"><path d="M3 5h18v14H3z" fill="none" stroke="#fff" stroke-width="2"/><path d="M3 6l9 7 9-7" fill="none" stroke="#fff" stroke-width="2"/></svg></span>
      </li>
      <li class="contact">
        <span>317 Birchfield Ln, Oakvane, NJ 07481</span>
        <span class="contact__icon"><svg viewBox="0 0 24 24" aria-hidden="true"><path d="M12 2a7 7 0 0 0-7 7c0 5.2 7 13 7 13s7-7.8 7-13a7 7 0 0 0-7-7zm0 9.5A2.5 2.5 0 1 1 12 6.5a2.5 2.5 0 0 1 0 5z"/></svg></span>
      </li>
    </ul>
  </section>
</main>
</body>
</html>
```